Modern Informational OBGYN website

Looking for a modern Wordpress website for a general OBGYN practice in Florida with a specialty in High Risk Obstetrics. We had an old Joomla website that crashed and we lost most of the files. It was over 10 years old and needed a refresh anyway.

Our practice serves a multicultural patient population (white, black, Spanish and Indian) and we would like our website to reflect that diversity. Our company colors are sunshine yellow (#ECBF6D) often combined with black, white and steel blue (#7191BE) in the "life" part of our logo (attached) depending on the background. Our tagline is "We're specialist in You!" Overall the site should have a clean modern yet comfortable feel. One that portrays friendliness and competence. At least 6 pages (Home, Obstetrics, Gynecology, News, Patient Education and Resources). Rotating stock pictures or videos are fine for the headers of the pages if the design you're considering calls for it. Interesting and creative use of typography and icons are encouraged.

The home page should have a call to action to schedule an appointment as well as a link to our patient portal. Other than the home and news pages, the other pages should have a similar look and feel. The home page should have sections on "About Us", "Medical Staff" (with pictures and brief bio for 2 male doctors, 2 female midwives and 1 female nurse practitioner), "Services" and "Location". The news page will be a closed blog that will not allow comments or responses. Both the obstetrics and the gynecology pages will have an educational blurb on the respective topics followed by a list of our services for each topic. Would be nice on the obstetrics page to have information and graphics changes that occur during each trimester (but not necessary). The resource page will have sections on at least "Office Forms", Office Policies", "OB Guide" each with multiple downloadable PDF's. Also a section on "Insurance" with a list of all the major insurance plans that we take with links to their company websites. The address, link and map to our hospital and their website can also go on this page. The Patient Education Page can be broken into 3 sections Obstetrics, Gynecology which both will have definition of medical disorders followed by FAQ's and "Helpful Links" which would have links to other website for medical information.

That's all that I can think of right now. The above is to help guide you but I am flexible, if the website design dictates a better flow of information. Looking forward to seeing what you can come up with. Down the road, I will be looking to the winning designer to produce matching brochures, full, half and quarter page media ads to have on hand for the practices further needs.

Target Market(s)

Women looking medical services

Industry/Entity Type

Medical

Coding

Coded - Design and coding required

Number of Pages Required

5+ page

Font styles to use
Sans Serif
Script

Colors

Designer to choose colors to be used in the design.

Requirements
Must have
• None. See projects description for suggestions
Nice to have
• infographics like information on stages of pregnancy on the obstetrics page

```html
<!DOCTYPE html>
<html lang="en">
<head>
<meta charset="utf-8">
<title>Brightday OB/GYN Services</title>
<link rel="stylesheet" href="https://fonts.googleapis.com/css2?family=Cinzel:wght@400;600&family=Montserrat:wght@400;500;600&display=swap">
<style>
:root{
  --sun:#ECBF6D;
  --sun-deep:#e5ad45;
  --steel:#7191BE;
  --steel-deep:#5f80b0;
  --ink:#222;
  --pale:#eef6fb;
  --white:#fff;
  --muted:#7a7a7a;
}
*{box-sizing:border-box;margin:0;padding:0}
html,body{width:1200px;height:5299px;overflow:hidden}
body{font-family:"Montserrat",sans-serif;color:var(--ink);background:var(--white)}
.page{position:relative;width:1200px;height:5299px;overflow:hidden}

/* header */
.site-header{position:absolute;left:0;top:0;width:1200px;height:82px;background:#fff;z-index:5}
.brand{position:absolute;left:180px;top:22px;display:flex;align-items:center;gap:8px}
.brand-dot{width:14px;height:14px;border-radius:50%;background:var(--sun)}
.brand-name{font-family:"Montserrat",sans-serif;font-weight:600;font-size:24px;color:var(--sun-deep);letter-spacing:1px;line-height:1}
.brand-sub{position:absolute;left:188px;top:56px;font-size:8px;letter-spacing:3px;color:#333;font-weight:600}
.main-nav{position:absolute;left:420px;top:0;height:82px;display:flex;align-items:center;font-size:12px;color:#333}
.main-nav a{color:inherit;text-decoration:none;padding:0 16px;height:82px;display:flex;align-items:center}
.main-nav a.active{background:var(--sun);color:#fff;padding:0 18px}
.search{position:absolute;left:1015px;top:30px}

/* hero */
.hero{position:absolute;left:0;top:82px;width:1200px;height:620px;background:var(--steel)}
.hero-photo{position:absolute;left:0;top:0;width:560px;height:620px;background:linear-gradient(160deg,#d9c3a6,#b59a73 55%,#e2c36d)}
.hero-text{position:absolute;right:160px;top:186px;text-align:right;color:#fff}
.hero-kicker{font-size:30px;letter-spacing:2px;font-weight:400}
.hero-title{font-family:"Cinzel",serif;font-size:64px;line-height:1.05;margin-top:6px;white-space:nowrap}
.hero-copy{font-size:11px;line-height:22px;margin-top:10px;width:490px;margin-left:auto}
.btn-outline{display:inline-block;margin-top:24px;border:1.5px solid #fff;border-radius:4px;padding:9px 14px;font-size:13px;color:#fff}
.hero-curve{position:absolute;left:0;top:530px}

/* shared section heads */
.sec-head{position:absolute;left:0;width:1200px;text-align:center}
.pill{display:inline-block;background:var(--sun);color:#fff;font-size:15px;padding:2px 10px;border-radius:12px}
.sec-title{font-family:"Cinzel",serif;font-size:34px;color:var(--steel);margin-top:12px;letter-spacing:1px;white-space:nowrap}
.sec-title b{color:var(--ink);font-weight:400}
.sec-head.on-blue .sec-title{color:#fff}
.sec-head.on-blue .sec-title b{color:var(--ink)}
.rule{display:block;margin:12px auto 0;width:54px;height:3px;background:linear-gradient(90deg,var(--steel),var(--sun))}

/* about */
.about-photo{position:absolute;box-shadow:0 4px 10px rgba(0,0,0,.2)}
.about-photo.one{left:163px;top:868px;width:306px;height:208px;background:linear-gradient(135deg,#cfd8df,#e5d9cc);border-top:3px solid var(--sun)}
.about-photo.two{left:288px;top:1002px;width:249px;height:229px;background:linear-gradient(160deg,#ece7e3,#e98aa3);border-bottom:3px solid var(--steel)}
.about-text{position:absolute;left:570px;top:866px;width:480px}
.about-text .sec-title{text-align:left;font-size:31px;margin-top:10px;letter-spacing:.5px}
.about-copy{font-size:11.5px;line-height:31px;color:#444;margin-top:14px}
.ticks{list-style:none;margin-top:8px}
.ticks li{font-size:11.5px;color:var(--steel);line-height:32px;display:flex;align-items:center;gap:6px;white-space:nowrap}

/* services */
.services-band{position:absolute;left:0;top:1266px}
.svc-card{position:absolute;background:#fff;display:flex;flex-direction:column;align-items:center;justify-content:center;text-align:center;box-shadow:0 4px 10px rgba(0,0,0,.12)}
.svc-card.featured{background:var(--sun);border:3px solid #fff}
.svc-card h3{font-family:"Cinzel",serif;font-weight:400;font-size:19px;color:var(--steel);margin-top:16px}
.svc-card.featured h3{color:#fff}
.svc-card .rule{margin-top:12px;width:100px}
.svc-card.featured .rule{background:#fff}

/* team */
.team-bg{position:absolute;left:0;top:2150px}
.team-card{position:absolute;width:424px;height:240px;padding:16px;display:flex;gap:18px;box-shadow:0 4px 10px rgba(0,0,0,.15);color:#fff}
.team-card.sun{background:var(--sun)}
.team-card.steel{background:var(--steel)}
.team-photo{width:158px;height:206px;flex:none;border:2px solid #fff}
.team-info h3{font-family:"Cinzel",serif;font-weight:400;font-size:20px;margin-top:14px}
.team-info p{font-size:10px;line-height:21px;margin-top:6px}
.btn-small{display:inline-flex;align-items:center;gap:6px;border:1px solid #fff;border-radius:3px;padding:4px 8px;font-size:10px;margin-top:12px}

/* blog */
.blog-card{position:absolute;top:3727px;width:274px;height:288px;background:#f6f6f6;box-shadow:0 2px 6px rgba(0,0,0,.08)}
.blog-img{width:274px;height:165px}
.blog-tag{position:absolute;left:20px;top:150px;display:flex;align-items:flex-end;gap:6px;font-size:12px;color:var(--sun-deep)}
.blog-tag i{display:block;width:36px;height:36px;background:var(--sun)}
.blog-cat{position:absolute;left:22px;top:200px;font-size:12px;color:#333}
.blog-title{position:absolute;left:22px;top:222px;width:240px;font-family:"Cinzel",serif;font-size:15px;line-height:26px;color:var(--steel)}
.pager{position:absolute;top:4062px;left:574px;display:flex;gap:12px}
.pager span{width:22px;height:22px;display:flex;align-items:center;justify-content:center}

/* contact */
.contact-band{position:absolute;left:0;top:4110px}
.map{position:absolute;left:163px;top:4482px;width:428px;height:251px;background:linear-gradient(135deg,#d8e6c8,#ede9df 60%,#bcd4ea)}
.info-row{position:absolute;left:163px;width:428px;height:34px;border:1px solid #fff;border-radius:4px;color:#fff;font-size:11px;display:flex;align-items:center;gap:10px;padding-left:12px}
.form-title{position:absolute;left:607px;top:4482px;font-family:"Cinzel",serif;color:#fff;font-size:34px}
.field{position:absolute;background:#fff;border-radius:4px;font-size:11px;color:#aaa;font-style:italic;padding:8px 12px;height:34px}
.submit{position:absolute;left:607px;top:4865px;width:432px;height:32px;background:var(--sun);border-radius:4px;color:#fff;font-family:"Cinzel",serif;font-size:18px;text-align:center;line-height:32px}

/* footer */
.footer{position:absolute;left:0;top:4975px;width:1200px;height:324px;background:var(--steel);color:#fff}
.footer-brand{position:absolute;left:0;width:1200px;top:60px;text-align:center}
.footer-brand .brand-name{color:#fff;font-size:40px}
.footer-brand small{display:block;font-size:10px;letter-spacing:5px;margin-top:6px;font-weight:600}
.footer-nav{position:absolute;top:160px;left:155px;width:885px;display:flex;justify-content:space-between;font-size:15px}
.footer-nav .active{font-weight:600}
.social{position:absolute;top:214px;left:530px;display:flex;gap:12px}
.social span{width:28px;height:28px;background:var(--sun)}
.copy{position:absolute;top:280px;width:1200px;text-align:center;font-size:11px}
.copy-rule{position:absolute;top:266px;left:410px;width:380px;height:1px;background:rgba(255,255,255,.4)}
</style>
</head>
<body>
<div class="page">

<header class="site-header">
  <div class="brand"><span class="brand-dot"></span><span class="brand-name">BRIGHTDAY</span></div>
  <div class="brand-sub">OB/GYN SERVICES</div>
  <nav class="main-nav">
    <a class="active">HOME</a><a>ABOUT US</a><a>MEDICAL STAFF</a><a>SERVICES</a><a>TEAM</a><a>LOCACTION</a>
  </nav>
  <svg class="search" width="20" height="20" viewBox="0 0 20 20"><circle cx="8" cy="8" r="6" fill="none" stroke="#ECBF6D" stroke-width="2"/><line x1="12.5" y1="12.5" x2="18" y2="18" stroke="#ECBF6D" stroke-width="2"/></svg>
</header>

<section class="hero">
  <div class="hero-photo" role="img" aria-label="Smiling young woman in a striped yellow sweater pointing to the headline"></div>
  <div class="hero-text">
    <div class="hero-kicker">A LIFETIME OF</div>
    <h1 class="hero-title">HEALTY SMILES</h1>
    <p class="hero-copy">Lorem Ipsum is simply dummy text of the printing and typesetting industry. Lorem Ipsum has been the industry's standard dummy text ever since the 1500s</p>
    <span class="btn-outline">MAKE AN APPOINTMENT</span>
  </div>
  <svg class="hero-curve" width="1200" height="100" viewBox="0 0 1200 100"><path d="M0 70 Q600 170 1200 40 L1200 100 L0 100Z" fill="#fff"/></svg>
</section>

<section class="about">
  <div class="about-photo one" role="img" aria-label="Mother and daughter at a clinic high-five"></div>
  <div class="about-photo two" role="img" aria-label="Cheerful woman in a pink hoodie giving an OK sign"></div>
  <div class="about-text">
    <span class="pill">ABOUT US</span>
    <h2 class="sec-title">BRIGHTDAY OB/GYN <b>SERVICES</b></h2>
    <p class="about-copy">Lorem Ipsum is simply dummy text of the printing and typesetting industry. Lorem Ipsum has been the industry's standard dummy text ever since the 1500s, when an unknown printer took a galley of type and scrambled it to make a type specimen book. It has survived not only five centuries, but also the leap into electronic typesetting</p>
    <ul class="ticks">
      <li><svg width="22" height="10" viewBox="0 0 22 10"><path d="M1 5l3 4 6-8M9 5l3 4 6-8" fill="none" stroke="#7191BE" stroke-width="1.3"/></svg>Lorem Ipsum is simply dummy text of the printing and typesetting.</li>
      <li><svg width="22" height="10" viewBox="0 0 22 10"><path d="M1 5l3 4 6-8M9 5l3 4 6-8" fill="none" stroke="#7191BE" stroke-width="1.3"/></svg>Lorem Ipsum is simply dummy text of the printing and typesetting.</li>
      <li><svg width="22" height="10" viewBox="0 0 22 10"><path d="M1 5l3 4 6-8M9 5l3 4 6-8" fill="none" stroke="#7191BE" stroke-width="1.3"/></svg>Lorem Ipsum is simply dummy text of the printing and typesetting.</li>
    </ul>
  </div>
</section>

<svg class="services-band" width="1200" height="940" viewBox="0 0 1200 940">
  <path d="M0 140 Q600 160 1200 0 L1200 70 Q600 170 0 160Z" fill="#ECBF6D"/>
  <path d="M0 130 Q600 150 1200 30 L1200 880 Q600 1010 0 880Z" fill="#7191BE"/>
  <path d="M0 880 Q600 1010 1200 880 L1200 940 L0 940Z" fill="#eef6fb"/>
</svg>

<div class="sec-head on-blue" style="top:1492px">
  <span class="pill">OUR SERVICES</span>
  <h2 class="sec-title">BRIGHTDAY OB/GYN <b>SERVICES</b></h2>
  <span class="rule"></span>
</div>

<div class="svc-card featured" style="left:163px;top:1636px;width:226px;height:226px">
  <svg width="96" height="96" viewBox="0 0 96 96" fill="none" stroke="#fff" stroke-width="3"><circle cx="46" cy="50" r="38"/><circle cx="46" cy="50" r="24"/><circle cx="46" cy="50" r="10"/><path d="M46 50L80 16M72 16h8v8"/></svg>
  <h3>OUR MISSION</h3><span class="rule"></span>
</div>
<div class="svc-card" style="left:407px;top:1636px;width:385px;height:226px">
  <svg width="100" height="90" viewBox="0 0 100 90" fill="none" stroke="#7191BE" stroke-width="3"><path d="M8 40l22-18 18 6 16-6 28 18-30 30-14-12-12 10z"/><path d="M50 6v10M34 10l4 8M66 10l-4 8"/></svg>
  <h3>OUR VISSION</h3><span class="rule"></span>
</div>
<div class="svc-card" style="left:809px;top:1636px;width:228px;height:226px">
  <svg width="100" height="90" viewBox="0 0 100 90" fill="none" stroke="#7191BE" stroke-width="3"><circle cx="50" cy="40" r="9"/><circle cx="24" cy="48" r="7"/><circle cx="76" cy="48" r="7"/><path d="M30 84c0-14 8-24 20-24s20 10 20 24zM8 84c0-10 6-18 16-18M92 84c0-10-6-18-16-18"/><path d="M50 8l3 6 6 1-4 4 1 6-6-3-6 3 1-6-4-4 6-1z"/></svg>
  <h3>MET THE TEAM</h3><span class="rule"></span>
</div>
<div class="svc-card" style="left:163px;top:1879px;width:226px;height:228px">
  <svg width="100" height="90" viewBox="0 0 100 90" fill="none" stroke="#7191BE" stroke-width="3"><circle cx="34" cy="14" r="7"/><circle cx="54" cy="14" r="7"/><circle cx="74" cy="14" r="7"/><path d="M22 40c0-10 6-16 12-16s12 6 12 16M42 40c0-10 6-16 12-16s12 6 12 16M62 40c0-10 6-16 12-16s12 6 12 16"/><path d="M10 66l18-12h22l-4 8H34M28 76h30l28-18"/></svg>
  <h3>CUSTOMER CARE</h3><span class="rule"></span>
</div>
<div class="svc-card" style="left:407px;top:1879px;width:385px;height:228px">
  <svg width="100" height="90" viewBox="0 0 100 90" fill="none" stroke="#7191BE" stroke-width="3"><circle cx="54" cy="24" r="18"/><path d="M36 24h36M54 6v36M42 12q12 12 0 24M66 12q-12 12 0 24"/><path d="M10 70l18-12h22l-4 8H34M28 80h30l28-18"/></svg>
  <h3>OUR SERVICES</h3><span class="rule"></span>
</div>
<div class="svc-card" style="left:809px;top:1879px;width:228px;height:228px">
  <svg width="100" height="90" viewBox="0 0 100 90" fill="none" stroke="#7191BE" stroke-width="3"><rect x="24" y="6" width="36" height="64" rx="5"/><path d="M36 14h12M44 40v-14M38 52l6-12 22 14-6 24H44z"/></svg>
  <h3>TOUCH WITH US</h3><span class="rule"></span>
</div>

<svg class="team-bg" width="1200" height="1230" viewBox="0 0 1200 1230">
  <rect x="0" y="42" width="1200" height="1100" fill="#eef6fb"/>
  <path d="M0 1110 Q600 1230 1200 1090 L1200 1230 L0 1230Z" fill="#ECBF6D"/>
  <path d="M0 1130 Q600 1250 1200 1120 L1200 1230 L0 1230Z" fill="#fff"/>
</svg>

<div class="sec-head" style="top:2338px">
  <span class="pill">TEAM</span>
  <h2 class="sec-title">BRIGHTDAY OB/GYN <b>SERVICES</b></h2>
  <span class="rule"></span>
</div>

<div class="team-card sun" style="left:163px;top:2484px">
  <div class="team-photo" role="img" aria-label="Portrait of a bearded male doctor" style="background:linear-gradient(160deg,#e8e8e8,#6b7ea0)"></div>
  <div class="team-info"><h3>NET RAYNOLDS</h3><p>Lorem Ipsum is simply dummy text of the printing and typesetting industry. Lorem Ipsum has been the industry's standard dummy text ever since the 1500s</p><span class="btn-small">LEARN MORE →</span></div>
</div>
<div class="team-card steel" style="left:611px;top:2484px">
  <div class="team-photo" role="img" aria-label="Portrait of a male doctor in a dark suit holding a phone" style="background:linear-gradient(160deg,#f2f2f2,#3b3b3b)"></div>
  <div class="team-info"><h3>NET RAYNOLDS</h3><p>Lorem Ipsum is simply dummy text of the printing and typesetting industry. Lorem Ipsum has been the industry's standard dummy text ever since the 1500s</p><span class="btn-small">LEARN MORE →</span></div>
</div>
<div class="team-card steel" style="left:163px;top:2750px">
  <div class="team-photo" role="img" aria-label="Portrait of a female midwife in a grey blazer" style="background:linear-gradient(160deg,#e4e4e4,#7a6d66)"></div>
  <div class="team-info"><h3>NET RAYNOLDS</h3><p>Lorem Ipsum is simply dummy text of the printing and typesetting industry. Lorem Ipsum has been the industry's standard dummy text ever since the 1500s</p><span class="btn-small">LEARN MORE →</span></div>
</div>
<div class="team-card sun" style="left:611px;top:2750px">
  <div class="team-photo" role="img" aria-label="Portrait of a female midwife holding a tablet" style="background:linear-gradient(160deg,#d3dff0,#8fa8cf)"></div>
  <div class="team-info"><h3>NET RAYNOLDS</h3><p>Lorem Ipsum is simply dummy text of the printing and typesetting industry. Lorem Ipsum has been the industry's standard dummy text ever since the 1500s</p><span class="btn-small">LEARN MORE →</span></div>
</div>
<div class="team-card sun" style="left:397px;top:3017px">
  <div class="team-photo" role="img" aria-label="Portrait of a nurse practitioner in blue scrubs" style="background:linear-gradient(160deg,#f0f0f0,#2f7fc0)"></div>
  <div class="team-info"><h3>NET RAYNOLDS</h3><p>Lorem Ipsum is simply dummy text of the printing and typesetting industry. Lorem Ipsum has been the industry's standard dummy text ever since the 1500s</p><span class="btn-small">LEARN MORE →</span></div>
</div>

<div class="sec-head" style="top:3571px">
  <span class="pill">OUR BLOG</span>
  <h2 class="sec-title">BRIGHTDAY OB/GYN <b>SERVICES</b></h2>
</div>

<article class="blog-card" style="left:163px">
  <div class="blog-img" role="img" aria-label="Man working at a desk with documents" style="background:linear-gradient(160deg,#eee,#b8b0a8)"></div>
  <div class="blog-tag"><i></i>Trending Now</div>
  <div class="blog-cat">Retirement</div>
  <h3 class="blog-title">PHYSICIANS CAN RETIRE TAX-FREE</h3>
</article>
<article class="blog-card" style="left:463px">
  <div class="blog-img" role="img" aria-label="Woman in a yellow top reading a document" style="background:linear-gradient(160deg,#f4f1ea,#e4b25a)"></div>
  <div class="blog-tag"><i></i>Most Popular</div>
  <div class="blog-cat">Retirement</div>
  <h3 class="blog-title">WORK TO 65 RETIRE AT 50</h3>
</article>
<article class="blog-card" style="left:763px">
  <div class="blog-img" role="img" aria-label="Laptop on a desk showing an investment screen" style="background:linear-gradient(160deg,#dfe3e7,#4a5663)"></div>
  <div class="blog-tag"><i></i>Advisor Topic</div>
  <div class="blog-cat">Retirement</div>
  <h3 class="blog-title">SUPPLEMENT 401K</h3>
</article>

<div class="pager">
  <span style="background:var(--sun)"><svg width="8" height="10" viewBox="0 0 8 10"><path d="M7 0v10L0 5z" fill="#fff"/></svg></span>
  <span style="background:var(--steel)"><svg width="8" height="10" viewBox="0 0 8 10"><path d="M1 0v10l7-5z" fill="#fff"/></svg></span>
</div>

<svg class="contact-band" width="1200" height="870" viewBox="0 0 1200 870">
  <path d="M0 20 Q600 150 1200 80 L1200 170 Q600 120 0 150Z" fill="#ECBF6D"/>
  <path d="M0 60 Q600 150 1200 100 L1200 870 L0 870Z" fill="#7191BE"/>
</svg>

<div class="sec-head on-blue" style="top:4351px">
  <span class="pill">OUR CONTACT</span>
  <h2 class="sec-title">BRIGHTDAY OB/GYN <b>SERVICES</b></h2>
</div>

<div class="map" role="img" aria-label="Street map showing the practice location"></div>
<div class="info-row" style="top:4766px"><svg width="12" height="14" viewBox="0 0 12 14"><path d="M6 13S1 8 1 5a5 5 0 0110 0c0 3-5 8-5 8z" fill="none" stroke="#fff" stroke-width="1.4"/><circle cx="6" cy="5" r="1.6" fill="#fff"/></svg>Lorem Ipsum is simply dummy text</div>
<div class="info-row" style="top:4814px"><svg width="12" height="12" viewBox="0 0 12 12"><path d="M2 1l2 0 1 3-1.5 1a7 7 0 003.5 3.5L8 7l3 1v2c0 1-1 1-1 1A10 10 0 011 2s0-1 1-1z" fill="#fff"/></svg>000 (55501) 24680</div>
<div class="info-row" style="top:4862px"><svg width="14" height="10" viewBox="0 0 14 10"><rect x=".7" y=".7" width="12.6" height="8.6" fill="none" stroke="#fff" stroke-width="1.3"/><path d="M1 1l6 5 6-5" fill="none" stroke="#fff" stroke-width="1.3"/></svg>www.brightdayobgyn.com</div>

<div class="form-title">GET IN TOUCH</div>
<div class="field" style="left:607px;top:4554px;width:210px">Name</div>
<div class="field" style="left:829px;top:4554px;width:210px">Last Name</div>
<div class="field" style="left:607px;top:4604px;width:432px">Phone</div>
<div class="field" style="left:607px;top:4653px;width:432px">Email</div>
<div class="field" style="left:607px;top:4702px;width:432px;height:148px">Message
  <svg style="position:absolute;right:6px;bottom:6px" width="22" height="22" viewBox="0 0 22 22"><path d="M2 20L20 2M10 20L20 10" stroke="#7191BE" stroke-width="1.5"/></svg>
</div>
<div class="submit">SUBMIT</div>

<footer class="footer">
  <div style="position:absolute;top:0;left:0;width:1200px;height:2px;background:#fff"></div>
  <div class="footer-brand">
    <div class="brand" style="position:static;display:inline-flex"><span class="brand-dot" style="background:#fff;width:18px;height:18px"></span><span class="brand-name">BRIGHTDAY</span></div>
    <small>OB/GYN SERVICES</small>
  </div>
  <nav class="footer-nav"><span class="active">HOME</span><span>ABOUT US</span><span>MEDICAL STAFF</span><span>SERVICES</span><span>TEAM</span><span>LOCACTION</span></nav>
  <div class="social"><span></span><span></span><span></span><span></span></div>
  <div class="copy-rule"></div>
  <div class="copy">Copyright © 2022 Brightday OB/GYN Services | All rights reserved</div>
</footer>

</div>
</body>
</html>
```